Post Card (5x7) - Pre-foreclosure Image - Harbor Path Partners

(Two-Sided Post Card)
FACING FORECLOSURE? YOU STILL HAVE OPTIONS.
If you’re behind on payments or at risk of foreclosure, you’re not alone—and it’s not too late to take action.
We help homeowners:
• Explore options to stay in their home
• Stop or delay foreclosure
• Sell quickly for a fair price if needed
No pressure. No obligation. Just real solutions tailored to your situation.
Call - (240) 558-2094
Email - marcus@hpbllc-mail.com
Harbor Path Partners LLC
7200 Bramwick Lane, Ellicott City, MD 21043
**Marcus Fennimore is a Licensed Realtor with Copperleaf Homes Realty in Bethesda, Maryland.
(Leave room for mailing address, return address & postage)
Target Market(s)
Distressed Homeowners
Industry/Entity Type
Real Estate

```html
<!DOCTYPE html>
<html lang="en">
<head>
<meta charset="utf-8">
<title>Harbor Path Partners – Pre-foreclosure Postcard</title>
<link href="https://fonts.googleapis.com/css2?family=Montserrat:ital,wght@0,400;0,500;0,600;0,700;0,800;1,700;1,800&family=Yellowtail&family=Roboto:wght@400;500&display=swap" rel="stylesheet">
<style>
:root{
  --bg:#8e8e8e;
  --ink:#111111;
  --black:#0a0a0a;
  --white:#ffffff;
  --panel:#f1f1f1;
  --tile:#ececec;
  --rule:#bdbdbd;
  --muted:#777777;
}
*{box-sizing:border-box;margin:0;padding:0}
html,body{width:833px;height:1200px;overflow:hidden}
body{background:var(--bg);position:relative;font-family:'Montserrat',sans-serif;color:var(--ink)}
.card{position:absolute;background:var(--white);overflow:hidden}
.card-front{left:62px;top:56px;width:707px;height:513px}
.card-back{left:62px;top:613px;width:710px;height:514px}
.art{position:absolute;left:0;top:0;width:100%;height:100%}
.front-panel{position:absolute;left:0;top:0;width:326px;height:420px;background:linear-gradient(180deg,#ededed 0%,#f7f7f7 60%,#ffffff 100%)}

.brand{position:absolute;text-align:center;font-family:'Montserrat',sans-serif;font-weight:500;letter-spacing:.14em}
.brand-name{display:block;font-size:21px;line-height:1}
.brand-sub{display:flex;align-items:center;justify-content:center;gap:8px;font-size:11px;margin-top:5px;letter-spacing:.22em}
.brand-sub::before,.brand-sub::after{content:"";display:block;width:46px;height:2px;background:currentColor}
.brand-front{left:0;width:326px;top:110px;color:var(--ink)}
.brand-back{left:72px;width:220px;top:164px;color:var(--white)}
.brand-back .brand-sub::before,.brand-back .brand-sub::after{width:38px}

.headline{position:absolute;left:0;width:326px;top:146px;text-align:center;font-weight:800;font-size:30px;line-height:31px;letter-spacing:-.01em}
.options-bar{position:absolute;left:35px;top:214px;width:259px;height:27px;background:var(--black);color:var(--white);font-weight:800;font-size:16px;line-height:27px;text-align:center}
.tagline{position:absolute;left:0;width:326px;top:254px;display:flex;align-items:center;justify-content:center;gap:8px;font-family:'Yellowtail',cursive;font-size:25px}
.tagline::before,.tagline::after{content:"";width:22px;height:1px;background:var(--ink)}

.service{position:absolute;top:295px;width:88px;height:119px}
.service-tile{position:absolute;left:0;top:31px;width:88px;height:88px;background:var(--tile)}
.service-badge{position:absolute;left:7px;top:0;width:75px;height:64px}
.service-text{position:absolute;left:0;top:70px;width:88px;text-align:center;font-size:10px;font-weight:500;line-height:12px}
.s1{left:29px}.s2{left:122px}.s3{left:214px}

.promise{position:absolute;left:34px;top:434px;font-style:italic;font-weight:800;font-size:16px;display:flex;gap:12px;align-items:center}
.promise span{display:flex;align-items:center;gap:5px}
.promise svg{width:13px;height:13px}
.solution{position:absolute;left:34px;top:455px;font-style:italic;font-weight:700;font-size:18px;letter-spacing:-.01em}

.agent-photo{position:absolute;left:43px;top:223px;width:86px;height:94px}
.agent{position:absolute;left:147px;top:218px;color:var(--white);font-family:'Roboto',sans-serif}
.agent-name{font-size:22px;font-weight:500;line-height:26px}
.agent-bio{font-size:10.5px;line-height:13px;margin-top:5px;width:190px}
.contact{position:absolute;left:146px;color:var(--white);font-family:'Montserrat',sans-serif;font-size:12.5px;display:flex;align-items:center;gap:7px}
.contact svg{width:13px;height:13px}
.c-phone{top:288px}.c-mail{top:305px}
.office{position:absolute;left:45px;top:331px;display:flex;gap:9px;color:var(--white);font-size:10.5px;line-height:13.5px}
.office svg{width:20px;height:24px;margin-top:1px}

.stamp{position:absolute;left:597px;top:19px;width:95px;height:102px;border:1.5px solid var(--muted)}
.address-line{position:absolute;left:440px;width:252px;height:1px;background:var(--rule)}
.l1{top:202px}.l2{top:263px}.l3{top:323px}.l4{top:384px}
</style>
</head>
<body>

<!-- FRONT -->
<section class="card card-front">
  <div class="front-panel"></div>
  <svg class="art" viewBox="0 0 1356 982" preserveAspectRatio="none" aria-hidden="false">
    <defs>
      <linearGradient id="sunsetCity" x1="0" y1="0" x2="0" y2="1">
        <stop offset="0" stop-color="#a7865a"/>
        <stop offset=".35" stop-color="#d39a45"/>
        <stop offset=".55" stop-color="#6a4318"/>
        <stop offset=".75" stop-color="#2a1a08"/>
        <stop offset="1" stop-color="#8a5a1e"/>
      </linearGradient>
    </defs>
    <polygon points="625,0 1356,0 1356,895 1204,982 625,652" fill="#111"/>
    <g role="img" aria-label="City skyline silhouetted against a golden sunset over a river">
      <polygon points="700,0 1356,0 1356,808 1204,895 700,602" fill="url(#sunsetCity)" stroke="#fff" stroke-width="5"/>
    </g>
  </svg>

  <div class="brand brand-front">
    <span class="brand-name">HARBOR PATH</span>
    <span class="brand-sub">PARTNERS LLC</span>
  </div>

  <h1 class="headline">FACING<br>FORECLOSURE?</h1>
  <div class="options-bar">YOU STILL HAVE OPTIONS.</div>
  <p class="tagline">We help homeowners</p>

  <div class="service s1">
    <div class="service-tile"></div>
    <svg class="service-badge" viewBox="0 0 75 64"><polygon points="0,0 75,0 75,44 37.5,64 0,44" fill="#111"/>
      <g fill="none" stroke="#fff" stroke-width="1.6"><path d="M22 28 L37 14 L52 28"/><path d="M26 25 V42 H36"/><circle cx="41" cy="35" r="6"/><path d="M45 39 L51 45"/></g></svg>
    <p class="service-text">Explore<br>options to stay<br>in their home</p>
  </div>
  <div class="service s2">
    <div class="service-tile"></div>
    <svg class="service-badge" viewBox="0 0 75 64"><polygon points="0,0 75,0 75,44 37.5,64 0,44" fill="#111"/>
      <g fill="none" stroke="#fff" stroke-width="1.6"><path d="M22 24 L35 12 L48 24"/><path d="M25 22 V42 H34"/><rect x="34" y="28" width="18" height="16"/><path d="M38 34 L46 26 M44 24 L49 29"/><path d="M37 40 H49"/></g></svg>
    <p class="service-text">Stop<br>or delay<br>foreclosure</p>
  </div>
  <div class="service s3">
    <div class="service-tile"></div>
    <svg class="service-badge" viewBox="0 0 75 64"><polygon points="0,0 75,0 75,44 37.5,64 0,44" fill="#111"/>
      <g fill="none" stroke="#fff" stroke-width="1.6"><path d="M18 26 L37.5 10 L57 26"/><path d="M23 22 V42 H52 V22"/><rect x="27" y="25" width="21" height="11" rx="2"/><path d="M37.5 36 V48"/></g>
      <text x="37.5" y="33.5" text-anchor="middle" font-family="Montserrat, sans-serif" font-size="7" font-weight="700" fill="#fff">SELL</text></svg>
    <p class="service-text">Sell quickly<br>for a fair price<br>if needed</p>
  </div>

  <p class="promise">
    <span><svg viewBox="0 0 14 14"><rect x="1" y="2" width="11" height="11" fill="none" stroke="#888" stroke-width="1.2"/><path d="M3.5 7 L6 9.5 L13 1.5" fill="none" stroke="#888" stroke-width="1.4"/></svg>No pressure.</span>
    <span><svg viewBox="0 0 14 14"><rect x="1" y="2" width="11" height="11" fill="none" stroke="#888" stroke-width="1.2"/><path d="M3.5 7 L6 9.5 L13 1.5" fill="none" stroke="#888" stroke-width="1.4"/></svg>No obligation.</span>
  </p>
  <p class="solution">Just real solutions tailored to your situation.</p>
</section>

<!-- BACK -->
<section class="card card-back">
  <svg class="art" viewBox="0 0 1361 985" preserveAspectRatio="none">
    <defs>
      <linearGradient id="eveningSky" x1="0" y1="0" x2="0" y2="1">
        <stop offset="0" stop-color="#b2331c"/>
        <stop offset=".35" stop-color="#e8731c"/>
        <stop offset=".6" stop-color="#f4b23a"/>
        <stop offset=".85" stop-color="#3a1a08"/>
        <stop offset="1" stop-color="#050505"/>
      </linearGradient>
      <linearGradient id="portrait" x1="0" y1="0" x2="0" y2="1">
        <stop offset="0" stop-color="#5b6b4a"/>
        <stop offset=".5" stop-color="#6e6a62"/>
        <stop offset="1" stop-color="#3b3d44"/>
      </linearGradient>
    </defs>
    <polygon points="0,0 755,0 755,655 174,985 0,888" fill="#111"/>
    <polygon points="0,0 682,0 682,605 172,898 0,800" fill="#050505" stroke="#fff" stroke-width="5"/>
    <g role="img" aria-label="City skyline silhouette against a fiery orange sunset sky">
      <rect x="0" y="0" width="679" height="235" fill="url(#eveningSky)"/>
    </g>
  </svg>

  <div class="brand brand-back">
    <span class="brand-name">HARBOR PATH</span>
    <span class="brand-sub">PARTNERS LLC</span>
  </div>

  <svg class="agent-photo" viewBox="0 0 86 94" role="img" aria-label="Portrait photo of Marcus Fennimore in a suit outdoors">
    <polygon points="0,0 86,0 86,74 43,94 0,74" fill="url(#portrait)"/>
  </svg>

  <div class="agent">
    <p class="agent-name">Marcus Fennimore</p>
    <p class="agent-bio">is a Licensed Realtor with Copperleaf Homes Realty in Bethesda, Maryland.</p>
  </div>
  <p class="contact c-phone"><svg viewBox="0 0 14 14"><path d="M3 1 L5.5 3.5 L4 5.5 Q5.5 8.5 8.5 10 L10.5 8.5 L13 11 L11 13 Q5 12.5 1 3 Z" fill="none" stroke="#fff" stroke-width="1"/></svg>(240) 558-2094</p>
  <p class="contact c-mail"><svg viewBox="0 0 14 14"><rect x="1" y="3" width="12" height="9" fill="none" stroke="#fff" stroke-width="1"/><path d="M1 3 L7 8.5 L13 3" fill="none" stroke="#fff" stroke-width="1"/></svg>marcus@hpbllc-mail.com</p>
  <div class="office">
    <svg viewBox="0 0 20 24"><path d="M10 18 C5 12 4 10 4 7.5 A6 6 0 0 1 16 7.5 C16 10 15 12 10 18 Z" fill="none" stroke="#fff" stroke-width="1.2"/><circle cx="10" cy="7.5" r="2.2" fill="none" stroke="#fff" stroke-width="1.2"/><path d="M6 16 Q1 18 4 21 Q10 23 16 21 Q19 18 14 16" fill="none" stroke="#fff" stroke-width="1.1"/></svg>
    <p>Harbor Path Partners LLC<br>7200 Bramwick Lane, Ellicott City,<br>MD 21043</p>
  </div>

  <div class="stamp"></div>
  <div class="address-line l1"></div>
  <div class="address-line l2"></div>
  <div class="address-line l3"></div>
  <div class="address-line l4"></div>
</section>

</body>
</html>
```